Masonry and Landscaping Construction company business card

Looking for a business card design for a construction company named Ferrante Construction. It is an italian-american family business that specializes in custom stone work, patios, walkways, driveways, steps, outdoor kitchens, concrete, waterproofing, power wash, landscaping and more. Our colors are mostly red and white with some black. We're looking for a bold design. we also like to incorporate a picture of my family's hometown somewhere in it.
Target Market(s)
Luxury home owners
Industry/Entity Type
Construction
Contact Information for Business Card
Details includes should be bullet points mentioning the services provided. Custom Stone Work, Outdoor Kitchens, Fire Pits, Patios, Walkways, Steps, Concrete, Waterproofing, powerwash and landscaping
Requirements
Must have
- Would like a spot on the card for co-owners names, numbers and email to be listed also looking to add the QR code for an instagram page
Nice to have
- would like something bold, based around the colors red and white with black outlines or details

```html
<!DOCTYPE html>
<html lang="en">
<head>
<meta charset="UTF-8">
<title>Ferrante Construction – Business Card</title>
<link href="https://fonts.googleapis.com/css2?family=Lato:wght@400;700;900&family=Montserrat:wght@500;700&display=swap" rel="stylesheet">
<style>
  :root {
    --red: #d8232a;
    --red-light: #e2443c;
    --red-deep: #c81d24;
    --white: #ffffff;
    --ink: #1b1b1b;
    --grey-light: #ececec;
    --grey-mid: #d2d2d2;
    --skyline: #c4c4c4;
  }
  * { margin: 0; padding: 0; box-sizing: border-box; }
  html, body {
    width: 1200px; height: 1000px; overflow: hidden;
    background: var(--white);
    font-family: "Lato", Arial, sans-serif;
  }
  .canvas { position: relative; width: 1200px; height: 1000px; }

  .card {
    position: absolute; left: 190px; width: 821px;
    border-radius: 18px; overflow: hidden;
  }

  /* Front */
  .card--front {
    top: 25px; height: 468px;
    background: linear-gradient(100deg, var(--red-light) 0%, var(--red) 55%, var(--red-deep) 100%);
  }
  .hometown-photo {
    position: absolute; left: 0; top: 0; width: 470px; height: 100%;
    background:
      linear-gradient(90deg, rgba(168,40,36,0.55) 0%, rgba(196,52,44,0.35) 55%, rgba(216,35,42,0) 100%),
      linear-gradient(180deg, rgba(226,90,70,0.5) 0%, rgba(170,46,38,0.45) 60%, rgba(150,40,34,0.5) 100%);
  }
  .brand-mark {
    position: absolute; left: 385px; top: 150px; width: 400px;
    text-align: center; color: var(--white);
    font-family: "Lato", Arial, sans-serif; font-weight: 900;
    font-size: 46px; line-height: 1.05; letter-spacing: 1px;
    text-transform: uppercase;
  }
  .services {
    position: absolute; left: 0; right: 0; top: 345px;
    text-align: center; color: var(--white);
    font-weight: 700; font-size: 21px; line-height: 26.5px;
    text-shadow: 0 1px 2px rgba(0,0,0,0.25);
  }
  .services .sep { font-style: italic; margin: 0 6px; }

  /* Back */
  .card--back {
    top: 507px; height: 468px;
    background: linear-gradient(90deg, var(--grey-light) 0%, #dedede 50%, var(--grey-mid) 100%);
  }
  .skyline-art {
    position: absolute; left: 5px; bottom: 0; width: 450px; height: 170px;
    background: linear-gradient(180deg, rgba(196,196,196,0) 0%, rgba(196,196,196,0.55) 35%, var(--skyline) 100%);
  }
  .brand-mark--small {
    position: absolute; left: 100px; top: 85px; width: 225px;
    text-align: center; color: var(--ink);
    font-weight: 900; font-size: 28px; line-height: 1.1;
    text-transform: uppercase; letter-spacing: 0.5px;
  }
  .person { position: absolute; left: 30px; top: 215px; width: 365px; text-align: center; }
  .person__name {
    font-family: "Montserrat", Arial, sans-serif; font-weight: 700;
    font-size: 30px; color: var(--red); letter-spacing: 0.5px; line-height: 1.1;
  }
  .person__role {
    font-family: "Montserrat", Arial, sans-serif; font-weight: 500;
    font-size: 22px; color: var(--ink); margin-top: 4px;
  }
  .contacts { position: absolute; left: 460px; top: 170px; list-style: none; }
  .contacts li {
    display: flex; align-items: flex-start;
    font-size: 22px; color: var(--ink); line-height: 29px; margin-bottom: 7px;
  }
  .contacts .icon {
    flex: 0 0 22px; width: 22px; height: 22px; margin: 3px 12px 0 0;
    background: var(--red); border-radius: 4px;
    display: flex; align-items: center; justify-content: center;
  }
</style>
</head>
<body>
<div class="canvas">

  <section class="card card--front">
    <div class="hometown-photo" role="img" aria-label="Photograph of the family's Italian hometown with a bell tower and domed church, tinted red"></div>
    <div class="brand-mark">Ferrante<br>Construction</div>
    <p class="services">
      Custom Stone Work<span class="sep">//</span>Outdoor Kitchens<span class="sep">//</span>Fire Pits<span class="sep">//</span>Patios<br>
      Walkways<span class="sep">//</span>Steps<span class="sep">//</span>Concrete<span class="sep">//</span>Waterproofing<br>
      powerwash and landscaping
    </p>
  </section>

  <section class="card card--back">
    <div class="skyline-art" role="img" aria-label="Faint city skyline with a construction crane"></div>
    <div class="brand-mark--small">Ferrante<br>Construction</div>
    <div class="person">
      <h1 class="person__name">MARCO BELLINI</h1>
      <p class="person__role">Marketing Executive</p>
    </div>
    <ul class="contacts">
      <li><span class="icon"><svg width="14" height="14" viewBox="0 0 24 24"><path fill="#fff" d="M6.6 10.8a15.1 15.1 0 006.6 6.6l2.2-2.2a1 1 0 011-.25 11.4 11.4 0 003.6.57 1 1 0 011 1V20a1 1 0 01-1 1A17 17 0 013 4a1 1 0 011-1h3.5a1 1 0 011 1c0 1.25.2 2.45.57 3.6a1 1 0 01-.25 1z"/></svg></span>044-555 201 347</li>
      <li><span class="icon"><svg width="14" height="14" viewBox="0 0 24 24"><path fill="#fff" d="M2 11l20-8-7 19-3-8z"/></svg></span>info@ferranteco.com</li>
      <li><span class="icon"><svg width="15" height="15" viewBox="0 0 24 24"><g fill="none" stroke="#fff" stroke-width="2"><circle cx="12" cy="12" r="9"/><path d="M3 12h18M12 3c3 3 3 15 0 18M12 3c-3 3-3 15 0 18"/></g></svg></span>www.ferranteco.com</li>
      <li><span class="icon"><svg width="14" height="14" viewBox="0 0 24 24"><path fill="#fff" d="M12 2a7 7 0 00-7 7c0 5 7 13 7 13s7-8 7-13a7 7 0 00-7-7zm0 9.5A2.5 2.5 0 1112 6.5a2.5 2.5 0 010 5z"/></svg></span>4417 Harbor View Rd,<br>210-B, FL 32551</li>
    </ul>
  </section>

</div>
</body>
</html>
```